Attention Getting Doorhanger Postcard Campaign offering HUGE Rebate on New Construction Homes

I am reestablishing my real estate career in the far North Dallas, TX area and want to offer a rebate on new construction homes to help get me started. I am requesting a doorhanger as my first project but would like a theme that I can carry over to other projects including postcards and other marketing items. I want it to look high end, clean, professional and classy. I am attaching a copy of a flier that I created that needs (no graphic designer here) some prettying up. But this is just to give you an idea of the type of style that is of interest to me.

Target Market(s)

Home buyers for new construction in far north dallas suburbs. Usually a move up buyer.

Industry/Entity Type

Real Estate

Colors

Designer to choose colors to be used in the design.

Requirements
Must have
• Catch phrase, draw attention, classy clean lines, current trend colors of blues and grays. My information, Harwood Fenn logo, equal housing and realtor logos. Fine Print: Not intended to solicit homes already listed for sale or buyers already in a buyers agency agreement with another brokerage. Please include offer details as listed in my flier. Again I am interested in a door hanger and the next round would be a flier or postcard.
Nice to have
• Picture of new homes that are in line with what is being built in my area. A few home builders sites: Silver Meadow, Brookvale Homes, Tenbury Homes, Calloway Homes.

```html
<!DOCTYPE html>
<html lang="en">
<head>
<meta charset="utf-8">
<title>Awe and then Some – Door Hangers</title>
<link href="https://fonts.googleapis.com/css2?family=Open+Sans:ital,wght@0,300;0,400;0,600;0,700;0,800;1,400&family=Roboto+Condensed:wght@300;400;700&family=Mr+Dafoe&display=swap" rel="stylesheet">
<style>
  :root{
    --maroon:#6e1f2d;
    --charcoal:#4a4a4c;
    --white:#ffffff;
    --ink:#222222;
    --muted:#8a8a8a;
    --backdrop:#e7e6e3;
    --panel-glass:rgba(255,255,255,.72);
  }
  *{margin:0;padding:0;box-sizing:border-box}
  html,body{width:1200px;height:1186px;overflow:hidden;background:var(--backdrop)}
  body{position:relative;font-family:"Open Sans",Arial,sans-serif;color:var(--ink)}

  .hanger{position:absolute;top:128px;width:406px;height:914px;background:var(--white);overflow:hidden;box-shadow:0 6px 18px rgba(0,0,0,.18)}
  .hanger--front{left:138px}
  .hanger--back{left:656px}

  .photo{position:absolute;left:0;top:0;width:406px;height:555px}
  .photo--stone{background:linear-gradient(180deg,#d9d1d0 0%,#b9a89a 30%,#8d7662 55%,#7a8060 78%,#8e8a80 100%)}
  .photo--white{background:linear-gradient(180deg,#c5c7c8 0%,#a9abad 28%,#c9c7c2 52%,#7d7469 74%,#6f7a5a 92%,#8c8a84 100%)}

  .facets{position:absolute;left:0;top:0;width:406px;height:555px}

  .hang-hole{position:absolute;left:139px;top:47px;width:130px;height:130px;border-radius:50%;background:var(--backdrop);box-shadow:inset 0 3px 6px rgba(0,0,0,.25)}

  .callout{position:absolute;top:193px;height:106px;background:var(--panel-glass)}
  .hanger--front .callout{left:11px;width:276px;padding:10px 10px 0 10px;font-size:15.5px;line-height:21px;font-weight:300;color:#2a2a2a}
  .callout strong{font-weight:700}
  .callout .accent{color:var(--maroon);font-weight:700}
  .hanger--back .callout{left:122px;width:273px;padding:16px 12px 0 0;text-align:right;font-size:25px;line-height:34px;font-weight:700;color:var(--maroon)}

  .lockup{position:absolute;top:0;left:0;width:406px;height:555px;color:var(--white)}
  .lockup .awe,.lockup .some{position:absolute;font-weight:800;line-height:1;letter-spacing:-1px}
  .lockup .awe{font-size:50px;top:477px}
  .lockup .some{font-size:56px;top:491px}
  .lockup .then{position:absolute;top:478px;font-size:18px;line-height:1;font-weight:400;letter-spacing:.5px}
  .hanger--front .awe{left:130px}
  .hanger--front .then{left:244px}
  .hanger--front .some{left:242px}
  .hanger--back .awe{left:22px}
  .hanger--back .then{left:137px}
  .hanger--back .some{left:134px}

  .band{position:absolute;left:0;width:406px}
  .band--steps{top:555px;height:92px;background:var(--charcoal);color:var(--white)}
  .band--offer{top:555px;height:92px;background:var(--charcoal);color:var(--white);text-align:center;padding-top:12px}
  .band--contact{top:797px;height:84px;background:var(--maroon);color:var(--white)}
  .band--rebates{top:797px;height:86px;background:var(--maroon);color:var(--white);text-align:center;padding-top:9px}

  .steps-title{position:absolute;left:10px;top:8px;font-family:"Roboto Condensed",Arial,sans-serif;font-weight:700;font-size:11px}
  .steps-line{position:absolute;left:66px;top:48px;width:330px;height:3px;background:var(--white)}
  .step{position:absolute;top:9px;width:90px;margin-left:-45px;text-align:center}
  .step-num{display:block;margin:0 auto;width:38px;height:38px;border-radius:50%;border:3px solid var(--white);background:var(--charcoal);font-size:15px;font-weight:600;line-height:32px;position:relative;z-index:1}
  .step-label{display:block;margin-top:9px;font-family:"Roboto Condensed",Arial,sans-serif;font-weight:300;font-size:11px;line-height:13px;text-transform:uppercase}

  .offer-line{font-size:15.5px;font-weight:300;line-height:21px}
  .offer-line strong{font-weight:700}
  .offer-line--big{font-size:18px;font-weight:700;line-height:24px}

  .brokerage{position:absolute;left:24px;top:690px;width:112px;font-size:13px;line-height:16px;font-weight:600;color:var(--maroon);display:flex;align-items:center;gap:6px;white-space:nowrap}
  .brokerage .mark{flex:none;width:9px;height:9px;background:var(--maroon)}
  .intro{position:absolute;left:148px;top:663px;width:236px;font-size:12px;line-height:17px;text-align:justify}
  .signature{position:absolute;right:20px;top:750px;font-family:"Mr Dafoe",cursive;font-size:27px;color:#c0203c}

  .headshot{position:absolute;left:23px;top:752px;width:106px;height:126px;border:3px solid var(--white);background:linear-gradient(160deg,#7a5a35 0%,#4e3a2a 45%,#2c2f46 100%);box-shadow:0 2px 5px rgba(0,0,0,.3);z-index:2}

  .credentials{position:absolute;left:148px;top:14px;font-size:12.5px;line-height:18.5px}

  .compliance{position:absolute;left:26px;top:892px;display:flex;gap:14px}
  .compliance span{width:18px;height:16px;background:#333}
  .fine-print{position:absolute;right:14px;top:888px;width:260px;text-align:right;font-family:"Roboto Condensed",Arial,sans-serif;font-weight:300;font-size:8.5px;line-height:11px;color:var(--muted)}

  .details{position:absolute;left:22px;top:661px;width:362px;font-size:11.6px;line-height:15.7px;text-align:justify}
  .details p+p{margin-top:8px}

  .rebate-line{font-size:15px;font-weight:300;line-height:22.5px}

  .get-in-touch{position:absolute;left:0;top:886px;width:406px;text-align:center;font-family:"Roboto Condensed",Arial,sans-serif;font-size:9.5px;color:var(--muted)}
  .get-in-touch .site{font-family:"Open Sans",Arial,sans-serif;font-style:italic;font-size:15px;color:var(--maroon);margin-left:5px}
</style>
</head>
<body>

<section class="hanger hanger--front">
  <div class="photo photo--stone" role="img" aria-label="Photo of a new stone and brick two-storey home at dusk with a paved walkway and planters"></div>
  <svg class="facets" viewBox="0 0 406 555" aria-hidden="true">
    <polygon points="240,0 406,0 406,190" fill="rgba(255,255,255,.18)"/>
    <polygon points="96,555 290,255 406,555" fill="rgba(255,255,255,.14)"/>
    <polygon points="0,555 0,430 96,555" fill="rgba(0,0,0,.08)"/>
  </svg>
  <div class="hang-hole"></div>
  <div class="callout">
    Receive a minimum of <strong>2.5%</strong><br>
    or more to put towards your<br>
    <span class="accent">NEW CONSTRUCTION<br>HOME!</span>
  </div>
  <div class="lockup">
    <span class="awe">AWE</span><span class="then">and then</span><span class="some">SOME</span>
  </div>

  <div class="band band--steps">
    <span class="steps-title">HOW IT WORKS:</span>
    <span class="steps-line"></span>
    <div class="step" style="left:109px"><span class="step-num">1</span><span class="step-label">Contact Dana<br>to register</span></div>
    <div class="step" style="left:190px"><span class="step-num">2</span><span class="step-label">Find your<br>new home</span></div>
    <div class="step" style="left:270px"><span class="step-num">3</span><span class="step-label">Sign your<br>contract</span></div>
    <div class="step" style="left:351px"><span class="step-num">4</span><span class="step-label">Close and receive<br>your rebate</span></div>
  </div>

  <div class="brokerage"><span class="mark"></span>Harwood Fenn</div>
  <p class="intro">I’ve sold hundreds of homes in the North Dallas area over the last 13 years, specializing in new construction homes. I would love to help you make your new home dreams a reality.</p>
  <div class="signature">Dana Whitcombe</div>

  <div class="headshot" role="img" aria-label="Portrait photo of the agent seated in a leather chair"></div>

  <div class="band band--contact">
    <p class="credentials">REALTOR®, CRS, ABR, CNHS, CHMS<br>Mobile: 555.014.2290<br>Email:&nbsp; dana@whitcombehomes.example</p>
  </div>

  <div class="compliance" aria-label="Compliance badges"><span></span><span></span></div>
  <p class="fine-print">Not intended to solicit properties that are already listed or buyers currently under a brokerage agreement with another Realtor</p>
</section>

<section class="hanger hanger--back">
  <div class="photo photo--white" role="img" aria-label="Photo of a new white-painted brick home with dark shutters and a lit front porch"></div>
  <svg class="facets" viewBox="0 0 406 555" aria-hidden="true">
    <polygon points="0,0 120,0 0,150" fill="rgba(255,255,255,.16)"/>
    <polygon points="0,0 130,0 300,555 120,555" fill="rgba(255,255,255,.10)"/>
    <polygon points="300,555 406,380 406,555" fill="rgba(0,0,0,.08)"/>
  </svg>
  <div class="hang-hole" style="left:138px"></div>
  <div class="callout">Maximize Your<br>Savings!</div>
  <div class="lockup">
    <span class="awe">AWE</span><span class="then">and then</span><span class="some">SOME</span>
  </div>

  <div class="band band--offer">
    <p class="offer-line">My Buy &amp; List package offers a <strong>FLAT FEE</strong></p>
    <p class="offer-line">on the sale of your current home.</p>
    <p class="offer-line offer-line--big">Saving you THOUSANDS!</p>
  </div>

  <div class="details">
    <p>We work with 100’s of builders in the local area so you are not limited to a few “select” builders. Homebuilders have the same bottom line sales price whether you have a REALTOR® representing you or not.</p>
    <p>Rebate program will not affect the price you pay for your home. Brokerage fees are paid through a separate marketing fund, not from the sales price of your home. Rebate program is in ADDITION to any builder or lender incentives.</p>
  </div>

  <div class="band band--rebates">
    <p class="rebate-line">$400,000 equals a $10,000 rebate!</p>
    <p class="rebate-line">$500,000 equals a $12,500 rebate!</p>
    <p class="rebate-line">*Lender approval required.</p>
  </div>

  <p class="get-in-touch">Get in touch with us any time:<span class="site">whitcombehomes.example</span></p>
</section>

</body>
</html>
```